Investment Firm Needs a Business Card Design

Need a business card for a new professional services firm that provides financial planning and investment management. Design should communicate financial safety and innovation. The contact information that needs to be on card is under Must Haves.

Target Market(s)

Retail Public

Industry/Entity Type

Investment

Requirements
Must have
• The data that needs to appear is in quotations:
"Daniel Hoskett, RWA"
(RWA logo either below my name or near my name)

"4417 Brambleton Lane
Suite 306
St. Charles, IL 60392"

"800-555-0143" (office)
"630-555-0187" (cell)
"dan@ledgerwisely.example" (email)
"www.LedgerWisely.example"
Nice to have
• would like to have the tag line "Steady Horizon(r)" with registered trade mark somewhere on card, maybe on back.

```html
<!DOCTYPE html>
<html lang="en">
<head>
<meta charset="utf-8">
<title>Ledger Wisely – Business Card</title>
<link href="https://fonts.googleapis.com/css2?family=Exo+2:wght@400;500;600&display=swap" rel="stylesheet">
<style>
  :root {
    --navy: #2b3568;
    --green: #3a9a48;
    --ink: #2a2a2e;
    --card: #ffffff;
    --card-shade: #eef0f2;
    --backdrop: #e4e6e9;
  }
  html, body {
    margin: 0;
    padding: 0;
    width: 1200px;
    height: 800px;
    overflow: hidden;
    background: var(--backdrop);
  }
  .canvas {
    position: relative;
    width: 1200px;
    height: 800px;
    display: flex;
    align-items: center;
    justify-content: center;
  }
  .card {
    position: relative;
    width: 1050px;
    height: 600px;
    background: linear-gradient(160deg, var(--card) 40%, var(--card-shade) 100%);
    box-shadow: 0 10px 30px rgba(0,0,0,0.12);
    overflow: hidden;
    font-family: "Exo 2", sans-serif;
    color: var(--ink);
  }
  .swoosh {
    position: absolute;
    inset: 0;
    width: 100%;
    height: 100%;
  }
  .holder {
    position: absolute;
    left: 82px;
    top: 92px;
  }
  .holder-name {
    margin: 0;
    font-size: 30px;
    font-weight: 500;
    letter-spacing: 0.5px;
  }
  .holder-title {
    margin: 6px 0 0 14px;
    font-size: 20px;
    font-weight: 400;
  }
  .contact {
    position: absolute;
    left: 98px;
    top: 255px;
    margin: 0;
    padding: 0;
    list-style: none;
    font-size: 17px;
    line-height: 31px;
    letter-spacing: 0.4px;
  }
  .contact li {
    display: flex;
    align-items: center;
    gap: 10px;
  }
  .contact .icon {
    width: 16px;
    height: 16px;
    fill: var(--ink);
    flex: none;
  }
  .contact .address {
    padding-left: 26px;
  }
  .brand {
    position: absolute;
    left: 540px;
    top: 190px;
    display: flex;
    align-items: center;
    gap: 14px;
  }
  .brand-square {
    width: 30px;
    height: 30px;
    background: var(--navy);
  }
  .brand-name {
    margin: 0;
    font-size: 44px;
    font-weight: 600;
    letter-spacing: 2px;
    text-transform: uppercase;
    color: var(--navy);
  }
</style>
</head>
<body>
<main class="canvas">
  <article class="card">
    <svg class="swoosh" viewBox="0 0 1050 600" preserveAspectRatio="none" aria-hidden="true">
      <path d="M0,528 C380,515 760,440 1050,318 L1050,600 L0,600 Z" fill="var(--navy)"/>
      <path d="M250,510 C560,490 820,410 1050,268 L1050,296 C820,432 560,500 250,510 Z" fill="var(--green)"/>
    </svg>

    <header class="holder">
      <h1 class="holder-name">Daniel Hoskett, RWA</h1>
      <p class="holder-title">consultant</p>
    </header>

    <div class="brand">
      <span class="brand-square"></span>
      <p class="brand-name">Ledger Wisely</p>
    </div>

    <ul class="contact">
      <li>
        <svg class="icon" viewBox="0 0 16 16"><path d="M3.5 1 L6 1 L7 5 L5.2 6.2 C6 8 8 10 9.8 10.8 L11 9 L15 10 L15 12.5 C15 13.9 13.9 15 12.5 15 C6.7 15 1 9.3 1 3.5 C1 2.1 2.1 1 3.5 1 Z"/></svg>
        <span>800-555-0143</span>
      </li>
      <li>
        <svg class="icon" viewBox="0 0 16 16"><path d="M4.5 0.5 H11.5 A1 1 0 0 1 12.5 1.5 V14.5 A1 1 0 0 1 11.5 15.5 H4.5 A1 1 0 0 1 3.5 14.5 V1.5 A1 1 0 0 1 4.5 0.5 Z M5 2.5 V12 H11 V2.5 Z M8 12.8 A0.9 0.9 0 1 0 8 14.6 A0.9 0.9 0 1 0 8 12.8 Z"/></svg>
        <span>630-555-0187</span>
      </li>
      <li>
        <svg class="icon" viewBox="0 0 16 16"><path d="M1 3 H15 V13 H1 Z M2.2 4 L8 8.6 L13.8 4 Z"/></svg>
        <span>dan@ledgerwisely.example</span>
      </li>
      <li>
        <svg class="icon" viewBox="0 0 16 16"><path d="M8 1 A7 7 0 1 0 8 15 A7 7 0 1 0 8 1 Z M8 2.4 C9 3.5 9.6 5 9.8 7.3 H6.2 C6.4 5 7 3.5 8 2.4 Z M2.5 8.7 H4.8 C4.9 10.6 5.4 12.2 6.2 13.3 A5.6 5.6 0 0 1 2.5 8.7 Z M2.5 7.3 A5.6 5.6 0 0 1 6.2 2.7 C5.4 3.8 4.9 5.4 4.8 7.3 Z M6.2 8.7 H9.8 C9.6 11 9 12.5 8 13.6 C7 12.5 6.4 11 6.2 8.7 Z M11.2 7.3 C11.1 5.4 10.6 3.8 9.8 2.7 A5.6 5.6 0 0 1 13.5 7.3 Z M11.2 8.7 H13.5 A5.6 5.6 0 0 1 9.8 13.3 C10.6 12.2 11.1 10.6 11.2 8.7 Z"/></svg>
        <span>www.LedgerWisely.example</span>
      </li>
      <li class="address">4417 Brambleton Lane, Suite 306</li>
      <li class="address">St. Charles, IL 60392</li>
    </ul>
  </article>
</main>
</body>
</html>
```